Cooler Trailer Rental Flyer

I need a flyer designed to showcase a rental product.

We own two refrigerated Chill Haulers. One trailer is 7’ x 12’. The second trailer is 7’ x 16’. Each unit is a double axle trailer with a cargo capacity of 8000 lbs. The refrigeration unit is 110v and is capable of cooling or freezing with just 12 amps. The 12’ unit comes with a securely mounted generator for stand-alone service needs, and we have a portable generator available if needed for the 16’ unit.

The trailer requires a class III or class IV hitch, with a 2 5/16” ball for towing and a 7-pin two vehicle socket for the trailer wiring.

We offer delivery for $1.40 per loaded mile (we only charge for the miles with the trailer attached, so one way for delivery or pickup). This option may make sense for many reasons, including:
- saving the cost of your time
- saving the cost of fuel
- eliminating your liability for the trailer while towing
- preventing you from having to buy any towing equipment

Our farm is located at 4127 Tamsen Mill Avenue, Byron Center, Michigan 49315. The name of the farm/business is Maple Hollow Farm.

The rental rates are as follows:
$169/day (two day minimum rental required)
$599/week
$1500/month

A $100 deposit is required to reserve the trailer. The deposit is fully refundable up to two weeks prior to the event, 50% up to one week, and non-refundable within one week of the event.

The website for the place we bought the trailer is www.frostvanhaul.example. A link to a video from his website is https://frostvanhaul.example/refrigerated-trailer-videos/

I would like the flyer to be colorful and professional, with photos.
Updates

Several notes: 1. I have added the logo for Maple Hollow Farm. 2. Contact information for the brochure should be as follows: Martin or Rebecca Kowalder Maple Hollow Farm 1874 Maple Hollow Lane SW Byron Center, MI 49315 (555) 014-7290 3. Please note that we are not "FrostVanHaul.example". This is the website for the manufacturer of the trailers.

Here are some rental ideas that might be worth including: Emergencies and Power Outages Food Distributors Food Vendors Restaurants Caterers Ice Vendors Pubs and Microbreweries Resorts Festivals Open Markets Sporting Events Parties Weddings Floral Distributors Meat Processors Hunters

e-mail address is maplehollowfarm@mailbox.example

Target Market(s)

Food distributors, caterers, resorts, events (festivals, weddings, fairs, parades, parties, concerts), restaurants, breweries, farmers markets, vending companies, big game hunters

Font styles to use
Serif
Sans Serif

Colors

Designer to choose colors to be used in the design.

Requirements
Nice to have
• Tri-fold flyer

```html
<!DOCTYPE html>
<html lang="en">
<head>
<meta charset="utf-8">
<title>Chill Haulers Rental Flyer</title>
<link href="https://fonts.googleapis.com/css2?family=Arimo:ital,wght@0,400;0,700;1,400&family=Roboto+Condensed:wght@400;700&display=swap" rel="stylesheet">
<style>
  :root {
    --green: #00963f;
    --yellow: #fff200;
    --ink: #161616;
  }
  html, body { margin: 0; padding: 0; width: 1200px; height: 855px; overflow: hidden; background: var(--green); }
  .stage { width: 1200px; height: 855px; overflow: hidden; position: relative; }
  .flyer {
    position: absolute; left: 0; top: 0;
    width: 1790px; height: 1275px;
    transform: scale(0.6704); transform-origin: 0 0;
    font-family: "Arimo", Arial, sans-serif;
    color: var(--ink);
  }
  .backdrop { position: absolute; left: 0; top: 0; width: 1790px; height: 1275px; }
  .badge-text {
    position: absolute; width: 104px; text-align: center;
    font-weight: 700; color: var(--yellow); font-size: 20px; line-height: 25px;
  }
  .delivery {
    position: absolute; left: 677px; top: 72px; width: 475px;
    font-size: 27px; line-height: 35px; letter-spacing: -0.6px;
    text-align: justify; margin: 0;
  }
  .delivery ul { list-style: none; margin: 0; padding: 0; }
  .delivery li { position: relative; padding-left: 24px; }
  .delivery li::before {
    content: ""; position: absolute; left: 1px; top: 11px;
    width: 15px; height: 15px; border-radius: 50%; background: var(--green);
  }
  .price-amount {
    position: absolute; color: var(--green); text-align: center;
    font-family: "Roboto Condensed", "Arial Narrow", sans-serif; font-weight: 700;
    font-size: 140px; line-height: 100px; height: 100px; letter-spacing: -7px; white-space: nowrap;
  }
  .price-amount .sign { font-size: 76px; letter-spacing: 0; margin-right: 6px; }
  .price-period {
    position: absolute; color: var(--green); text-align: center;
    font-weight: 700; font-size: 48px; line-height: 48px; height: 48px;
    letter-spacing: 1px; white-space: nowrap;
  }
  .minimum-note {
    position: absolute; left: 388px; top: 648px; width: 160px;
    text-align: center; font-style: italic; color: var(--green);
    font-size: 24px; line-height: 30px; letter-spacing: 0.5px;
  }
  .fleet {
    position: absolute; left: 40px; top: 830px; width: 540px;
    text-align: center; font-size: 23px; line-height: 30.2px; letter-spacing: -0.6px;
  }
  .fleet p { margin: 0 0 30px; }
  .rates-heading {
    position: absolute; left: 1270px; top: 824px; width: 436px; margin: 0;
    text-align: center; color: var(--yellow);
    font-family: "Roboto Condensed", "Arial Narrow", sans-serif; font-weight: 700;
    font-size: 35px; line-height: 44px; letter-spacing: -0.5px;
  }
  .rate-list { position: absolute; left: 1295px; top: 908px; margin: 0; padding: 0; list-style: none; }
  .rate-list li { color: var(--yellow); font-size: 24px; height: 43px; white-space: nowrap; letter-spacing: -0.5px; }
  .rate-list b { font-size: 32px; letter-spacing: -1px; }
  .rate-list small { color: var(--ink); font-size: 19px; letter-spacing: -0.4px; }
  .deposit {
    position: absolute; left: 1258px; top: 1068px; width: 460px; margin: 0;
    text-align: justify; font-size: 23px; line-height: 31px; letter-spacing: -0.6px;
  }
  .deposit .hi { color: var(--yellow); }
  .deposit .hi b { font-size: 32px; }
</style>
</head>
<body>
<div class="stage">
<div class="flyer">
  <svg class="backdrop" viewBox="0 0 1790 1275" xmlns="http://www.w3.org/2000/svg">
    <defs>
      <linearGradient id="outdoorTone" x1="0" y1="0" x2="0" y2="1">
        <stop offset="0" stop-color="#e9eaec"/>
        <stop offset="0.75" stop-color="#d3d4d4"/>
        <stop offset="1" stop-color="#9a9b92"/>
      </linearGradient>
      <linearGradient id="insideTone" x1="0" y1="0" x2="0" y2="1">
        <stop offset="0" stop-color="#cfd1d3"/>
        <stop offset="1" stop-color="#eeeeee"/>
      </linearGradient>
    </defs>
    <rect width="1790" height="1275" fill="var(--green)"/>
    <rect x="610" y="40" width="593" height="770" fill="var(--yellow)"/>
    <path d="M0,420 C150,480 220,590 300,590 C380,590 520,430 610,430 C700,430 820,590 900,590 C980,590 1110,430 1200,430 C1290,430 1420,590 1500,590 C1580,590 1700,480 1790,430 V810 H0 Z" fill="var(--yellow)"/>
    <path role="img" aria-label="Photo: rear doors of a white enclosed refrigerated trailer" d="M40,40 H610 V430 C520,430 380,590 300,590 C220,590 150,480 40,440 Z" fill="url(#outdoorTone)"/>
    <path role="img" aria-label="Photo: side view of a white double axle cooler trailer with its refrigeration unit" d="M1203,40 H1752 V455 C1700,482 1580,590 1500,590 C1420,590 1290,430 1203,430 Z" fill="url(#outdoorTone)"/>
    <path d="M0,420 C150,480 220,590 300,590 C380,590 520,430 610,430 C700,430 820,590 900,590 C980,590 1110,430 1200,430 C1290,430 1420,590 1500,590 C1580,590 1700,480 1790,430" fill="none" stroke="var(--green)" stroke-width="32"/>
    <rect role="img" aria-label="Photo: white insulated interior of the cooler trailer with strip curtain" x="610" y="810" width="588" height="428" fill="url(#insideTone)"/>
    <g fill="var(--green)">
      <polygon points="85,563 137,590 137,637 85,664 33,637 33,590"/>
      <polygon points="705,563 757,590 757,637 705,664 653,637 653,590"/>
      <polygon points="1315,563 1367,590 1367,637 1315,664 1263,637 1263,590"/>
    </g>
  </svg>

  <div class="badge-text" style="left:33px;top:576px;">The<br>rental<br>rates</div>
  <div class="badge-text" style="left:653px;top:576px;">The<br>rental<br>rates</div>
  <div class="badge-text" style="left:1263px;top:576px;">The<br>rental<br>rates</div>

  <div class="delivery">
    We offer delivery for $1.40 per loaded mile (we only charge for the miles with the trailer attached, so one way for delivery or pickup). This option may make sense for many reasons, including:
    <ul>
      <li>saving the cost of your time</li>
      <li>saving the cost of fuel</li>
      <li>eliminating your liability for the trailer while towing</li>
      <li>preventing you from having to buy any towing equipment</li>
    </ul>
  </div>

  <div class="price-amount" style="left:122px;top:640px;width:260px;"><span class="sign">$</span>169</div>
  <div class="price-period" style="left:122px;top:746px;width:260px;">PER DAY</div>
  <div class="minimum-note">(TWO DAY MINIMUM RENTAL REQUIRED)</div>

  <div class="price-amount" style="left:742px;top:634px;width:320px;"><span class="sign">$</span>1500</div>
  <div class="price-period" style="left:742px;top:739px;width:320px;">PER MONTH</div>

  <div class="price-amount" style="left:1345px;top:640px;width:260px;"><span class="sign">$</span>599</div>
  <div class="price-period" style="left:1345px;top:746px;width:260px;">PER WEEK</div>

  <div class="fleet">
    <p>We own two refrigerated Chill Haulers.<br>One trailer is 7’ x 12’.<br>The second trailer is 7’ x 16’.<br>Each unit is a double axle trailer with a cargo capacity of 8000 lbs. The refrigeration unit is 110v and is capable of cooling or freezing with just 12 amps. The 12’ unit comes with a securely mounted generator for stand-alone service needs, and we have a portable generator available if needed for the 16’ unit.</p>
    <p>The trailer requires a class III or class IV hitch, with a 2 5/16” ball for towing and a 7-pin two vehicle socket for the trailer wiring.</p>
  </div>

  <h2 class="rates-heading">THE RENTAL RATES ARE<br>AS FOLLOWS:</h2>
  <ul class="rate-list">
    <li>$<b>169</b>/day <small>(two day minimum rental required)</small></li>
    <li>$<b>599</b>/week</li>
    <li>$<b>1500</b>/month</li>
  </ul>

  <p class="deposit">A <span class="hi">$<b>100</b></span> deposit is required to reserve the trailer. The deposit is fully refundable up to two weeks prior to the event, <span class="hi"><b>50</b>% up to one week</span>, and non-refundable within one week of the event.</p>
</div>
</div>
</body>
</html>
```